Business Card Design

Cedar Gate Rentals
Cedar Gate Rentals is a high end home rental leasing company that provides exquisite properties in niche markets. We are a small family owned business that considers our clients not as renters, but as friends. Every property we buy must be brought up to our high standards before it is offered on the market. The properties that we lease are exceptional, "move in" ready homes. This allows for the client to take pride in their lease as if it was their own home. To put it another way; we do not lease a property that we would not live in ourselves.

Target Market(s)

Couples making $100K or more

Industry/Entity Type

Business

Requirements
Must have
• Some sort of logo
Nice to have
• good slogan
Should not have
• Pink

```html
<!DOCTYPE html>
<html lang="en">
<head>
<meta charset="utf-8">
<title>Cedar Gate Rentals – Business Card</title>
<link rel="stylesheet" href="https://fonts.googleapis.com/css2?family=Cinzel:wght@600;700&family=Ubuntu:wght@400;500;700&display=swap">
<style>
  :root {
    --backdrop: #8a97a3;
    --brown: #782a1d;
    --paper: #ffffff;
    --ink: #7a2b1e;
  }
  * { margin: 0; padding: 0; box-sizing: border-box; }
  html, body {
    width: 1200px;
    height: 1000px;
    overflow: hidden;
    background: var(--backdrop);
  }
  .card {
    position: absolute;
    left: 100px;
    top: 215px;
    width: 1000px;
    height: 570px;
    background: var(--paper);
    box-shadow: 0 10px 30px rgba(0,0,0,.25);
    overflow: hidden;
  }
  .brand-panel {
    position: absolute;
    left: 0; top: 0;
    width: 450px;
    height: 100%;
    background: var(--brown);
    overflow: hidden;
  }
  .brand-panel__rule {
    position: absolute;
    left: 0;
    top: 538px;
    width: 100%;
    height: 6px;
    background: var(--paper);
  }
  .company-name {
    position: absolute;
    left: 40px;
    right: 30px;
    top: 96px;
    font-family: "Cinzel", serif;
    font-weight: 700;
    font-size: 31px;
    letter-spacing: 0.5px;
    color: var(--paper);
    white-space: nowrap;
  }
  .brand-mark {
    position: absolute;
    left: 0;
    width: 100%;
    top: 300px;
    display: flex;
    justify-content: center;
    align-items: center;
    gap: 12px;
  }
  .brand-mark__square {
    width: 22px;
    height: 22px;
    background: var(--paper);
  }
  .brand-mark__name {
    font-family: "Cinzel", serif;
    font-weight: 700;
    font-size: 26px;
    color: var(--paper);
    white-space: nowrap;
  }
  .contact-panel__rule {
    position: absolute;
    left: 450px;
    right: 0;
    top: 510px;
    height: 6px;
    background: var(--brown);
  }
  .person {
    position: absolute;
    right: 62px;
    top: 52px;
    text-align: right;
    color: var(--ink);
    font-family: "Ubuntu", sans-serif;
  }
  .person__name {
    font-weight: 700;
    font-size: 32px;
    line-height: 1.1;
  }
  .person__title {
    font-weight: 400;
    font-size: 20px;
    margin-right: -40px;
  }
  .contact-list {
    position: absolute;
    right: 50px;
    top: 365px;
    list-style: none;
    text-align: right;
    font-family: "Ubuntu", sans-serif;
    font-weight: 500;
    font-size: 26px;
    line-height: 1.45;
    color: var(--ink);
  }
</style>
</head>
<body>
  <div class="card">
    <section class="brand-panel">
      <h1 class="company-name">Cedar Gate Rentals</h1>
      <div class="brand-mark">
        <span class="brand-mark__square"></span>
        <span class="brand-mark__name">Cedar Gate Rentals</span>
      </div>
      <div class="brand-panel__rule"></div>
    </section>

    <div class="person">
      <div class="person__name">Your Name</div>
      <div class="person__title">Title</div>
    </div>

    <ul class="contact-list">
      <li>Phone : 123- 456-7890</li>
      <li>E-mail : yourname@mail.com</li>
      <li>Website : www.address.com</li>
    </ul>

    <div class="contact-panel__rule"></div>
  </div>
</body>
</html>
```